BUsiness Card

We need a unique business card design for a new aesthetic practice, Meadowlark Skin & Vitality, P.A. The reverse of the card should be an appointment card.

```html
<!DOCTYPE html>
<html lang="en">
<head>
<meta charset="utf-8">
<title>Meadowlark Skin &amp; Vitality – Business Card</title>
<link rel="stylesheet" href="https://fonts.googleapis.com/css2?family=Cinzel:wght@600;700&family=Roboto:wght@400&family=Roboto+Condensed:ital,wght@0,700;1,400&display=swap">
<style>
  :root{
    --backdrop:#2b2b2b;
    --card:#f3f3f3;
    --navy:#0f4a66;
    --teal:#3fa8ae;
    --ink:#555a5e;
    --dots:#7a8288;
    --faint:#e4e6e8;
  }
  *{margin:0;padding:0;box-sizing:border-box}
  html,body{width:1200px;height:960px;overflow:hidden;background:var(--backdrop)}
  .card{position:absolute;width:600px;height:342px;background:var(--card);border-radius:22px;overflow:hidden}
  .card--front{left:302px;top:119px}
  .card--back{left:299px;top:498px}
  .bg-mark{position:absolute;right:-60px;top:20px;width:330px;height:330px;border-radius:50%;background:var(--faint)}
  .card--back .bg-mark{right:-40px;top:40px}

  .brand{position:absolute;left:50px;top:92px;width:236px;text-align:center}
  .brand__dot{width:88px;height:88px;border-radius:50%;background:var(--navy);margin:0 auto 14px}
  .brand__name{font-family:"Cinzel",serif;font-weight:700;color:var(--navy);font-size:21px;line-height:26px}

  .contact{position:absolute;left:323px;top:78px;font-family:"Roboto",sans-serif;color:var(--ink)}
  .contact__name{font-family:"Cinzel",serif;font-weight:700;color:var(--navy);font-size:25px;line-height:28px}
  .contact__title{font-family:"Cinzel",serif;font-weight:600;color:var(--teal);font-size:15px;line-height:18px;margin-bottom:8px}
  .contact__company{font-family:"Roboto Condensed",sans-serif;font-weight:700;font-size:14px;line-height:18px}
  .contact__line{font-size:15px;line-height:18px}
  .contact__list{list-style:none;margin-top:12px}
  .contact__list li{display:flex;align-items:center;gap:8px;font-size:15px;line-height:19px}
  .contact__list svg{width:13px;height:13px;fill:var(--navy)}

  .appt{position:absolute;inset:0;padding:28px 34px 0 35px;font-family:"Roboto",sans-serif;color:var(--navy)}
  .appt__title{font-family:"Cinzel",serif;font-weight:700;font-size:21px;text-align:center;letter-spacing:.5px;margin-bottom:10px}
  .field{display:flex;align-items:baseline;font-size:18px;height:46px}
  .field__fill{flex:1;border-bottom:1.5px dotted var(--dots);margin-left:4px;transform:translateY(-3px)}
  .field__unit{font-size:14px;margin-left:4px}
  .field--gap{margin-left:0}
  .field--blank{height:40px}
  .appt__notice{position:absolute;left:0;right:0;top:282px;text-align:center;font-family:"Roboto Condensed",sans-serif;font-style:italic;font-size:14px;line-height:17px;color:var(--ink)}
</style>
</head>
<body>
  <section class="card card--front">
    <div class="bg-mark"></div>
    <div class="brand">
      <div class="brand__dot"></div>
      <div class="brand__name">Meadowlark<br>Skin &amp; Vitality</div>
    </div>
    <div class="contact">
      <h1 class="contact__name">Daniel Hartwell</h1>
      <p class="contact__title">CEO/FOUNDER</p>
      <p class="contact__company">Meadowlark Skin &amp; Vitality, P.A.</p>
      <p class="contact__line">4120 Willow Bend Road</p>
      <p class="contact__line">Juneau, Alaska 99801</p>
      <ul class="contact__list">
        <li><svg viewBox="0 0 24 24"><path d="M6.6 10.8a15.1 15.1 0 0 0 6.6 6.6l2.2-2.2a1 1 0 0 1 1-.25 11.4 11.4 0 0 0 3.6.57 1 1 0 0 1 1 1V20a1 1 0 0 1-1 1A17 17 0 0 1 3 4a1 1 0 0 1 1-1h3.5a1 1 0 0 1 1 1c0 1.25.2 2.45.57 3.57a1 1 0 0 1-.25 1z"/></svg>(907) 555-0143</li>
        <li><svg viewBox="0 0 24 24"><path d="M2 5h20v14H2zM3 6.5v1l9 6 9-6v-1z"/></svg>dhartwell@meadowlarkskin.com</li>
        <li><svg viewBox="0 0 24 24"><circle cx="12" cy="12" r="10"/><path d="M2 12h20M12 2c3 3 3 17 0 20M12 2c-3 3-3 17 0 20" stroke="#f3f3f3" stroke-width="1.6" fill="none"/></svg>www.meadowlarkskin.com</li>
      </ul>
    </div>
  </section>

  <section class="card card--back">
    <div class="bg-mark"></div>
    <div class="appt">
      <h2 class="appt__title">NEXT APPOINTMENT</h2>
      <div class="field">Name:<span class="field__fill"></span></div>
      <div class="field">Date:<span class="field__fill"></span>Time:<span class="field__fill" style="flex:0 0 115px"></span><span class="field__unit">AM/PM</span></div>
      <div class="field">Note:<span class="field__fill"></span></div>
      <div class="field field--blank"><span class="field__fill field--gap"></span></div>
      <div class="field field--blank"><span class="field__fill field--gap"></span></div>
      <p class="appt__notice">Please give me 24 hours notice if you are unable to keep your<br>appointment or a cancellation fee may be charged.</p>
    </div>
  </section>
</body>
</html>
```